International Trading Company, 'VOLA' needs a Business Card

The company name is "VOLA" and it has own logo design.
I'd like to use its logo on this business card.
I need two side Business Card.
I'll look forward to your great design.
Thank you very much in advance.

Contact Information for Business Card

Company Name : Vola Harbor Limited
Information Example
Tobias Wrenfold
Mobile(use icon please) : 1 (555) 014-2290
Tel(use icon please) : 1 (555) 014-6835
Email(use icon please) : tobias27@volaharbor.example
Address(use icon please) : 482 Larkmoor Rd, New York, NY 10199, USA

```html
<!DOCTYPE html>
<html lang="en">
<head>
<meta charset="utf-8">
<title>VOLA Business Card</title>
<link rel="stylesheet" href="https://fonts.googleapis.com/css2?family=Exo+2:wght@400;700&display=swap">
<style>
  :root {
    --bg: #e9e9ea;
    --card-dark: #5a5a5c;
    --card-dark-edge: #4a4a4c;
    --card-light: #ffffff;
    --ink: #4b4b4d;
    --ink-soft: #6a6a6c;
    --band: #5c5c5e;
    --band-dark: #4a4a4c;
    --white: #ffffff;
  }
  * { margin: 0; padding: 0; box-sizing: border-box; }
  html, body {
    width: 1200px; height: 929px; overflow: hidden;
    background: var(--bg);
    font-family: "Exo 2", sans-serif;
  }
  .canvas { position: relative; width: 1200px; height: 929px; }
  .card {
    position: absolute; width: 600px; height: 343px;
    border-radius: 16px; overflow: hidden;
    box-shadow: 0 10px 30px rgba(0,0,0,0.18);
  }
  /* Front */
  .card-front {
    left: 120px; top: 100px;
    background: linear-gradient(135deg, var(--card-dark) 0%, var(--card-dark-edge) 100%);
  }
  .front-map {
    position: absolute; left: 90px; top: 70px; width: 420px; height: 200px;
    background: radial-gradient(ellipse at center, rgba(255,255,255,0.12) 0%, rgba(255,255,255,0.04) 60%, rgba(255,255,255,0) 100%);
  }
  .front-name {
    position: absolute; left: 0; right: 0; top: 130px;
    text-align: center; color: var(--white);
    font-weight: 700; font-size: 78px; letter-spacing: 2px; line-height: 1;
  }
  /* Back */
  .card-back {
    left: 480px; top: 486px;
    background: var(--card-light);
  }
  .back-art { position: absolute; inset: 0; }
  .back-name {
    position: absolute; left: 42px; top: 128px;
    color: var(--ink); font-weight: 700; font-size: 64px; letter-spacing: 1px; line-height: 1;
  }
  .holder {
    position: absolute; right: 30px; top: 34px; text-align: right; color: var(--ink);
  }
  .holder-name { font-size: 19px; letter-spacing: 0.5px; text-transform: uppercase; }
  .holder-title { font-size: 13px; color: var(--ink-soft); margin-top: 1px; }
  .name-rule {
    position: absolute; left: 300px; top: 92px; width: 270px; height: 1px; background: var(--ink);
  }
  .address {
    position: absolute; right: 30px; top: 104px; text-align: right;
    font-size: 12.5px; line-height: 1.45; color: var(--ink-soft);
  }
  .contact-rule {
    position: absolute; left: 36px; top: 230px; width: 220px; height: 1px; background: var(--ink);
  }
  .contacts {
    position: absolute; left: 36px; top: 242px; list-style: none;
    font-size: 13px; color: var(--ink); line-height: 1;
  }
  .contacts li { display: flex; align-items: center; gap: 10px; margin-bottom: 7px; }
  .contacts svg { width: 12px; height: 12px; flex: none; }
</style>
</head>
<body>
<div class="canvas">

  <section class="card card-front" aria-label="Card front">
    <div class="front-map" role="img" aria-label="Faint dotted world map"></div>
    <div class="front-name">VOLA</div>
  </section>

  <section class="card card-back" aria-label="Card back">
    <svg class="back-art" viewBox="0 0 600 343" width="600" height="343" aria-hidden="true">
      <path d="M0,322 C190,322 300,312 370,240 C420,190 480,168 600,168 L600,343 L0,343 Z" fill="var(--band)"/>
      <path d="M0,328 C200,326 310,318 380,250 C430,200 490,180 600,178" fill="none" stroke="var(--white)" stroke-width="4"/>
      <path d="M0,335 L600,335 L600,343 L0,343 Z" fill="var(--band-dark)"/>
      <path d="M600,28 A14,14 0 0 0 600,56 Z" fill="var(--band)"/>
    </svg>

    <div class="back-name">VOLA</div>

    <div class="holder">
      <div class="holder-name">Tobias Wrenfold</div>
      <div class="holder-title">Founder</div>
    </div>
    <div class="name-rule"></div>
    <div class="address">482 Larkmoor Rd, New York,<br>NY 10199, USA</div>

    <div class="contact-rule"></div>
    <ul class="contacts">
      <li>
        <svg viewBox="0 0 12 12"><rect x="3" y="0.5" width="6" height="11" rx="1" fill="none" stroke="var(--ink)" stroke-width="1"/><line x1="5" y1="9.5" x2="7" y2="9.5" stroke="var(--ink)"/></svg>
        1 (555) 014-2290
      </li>
      <li>
        <svg viewBox="0 0 12 12"><path d="M2.5,1 L4.5,1 L5.2,3.8 L3.9,4.8 C4.6,6.4 5.6,7.4 7.2,8.1 L8.2,6.8 L11,7.5 L11,9.5 C11,10.3 10.3,11 9.5,11 C5,10.6 1.4,7 1,2.5 C1,1.7 1.7,1 2.5,1 Z" fill="var(--ink)"/></svg>
        1 (555) 014-6835
      </li>
      <li>
        <svg viewBox="0 0 12 12"><rect x="0.5" y="2.5" width="11" height="7.5" fill="var(--ink)"/><path d="M0.8,2.8 L6,7 L11.2,2.8" fill="none" stroke="var(--white)" stroke-width="1"/></svg>
        tobias27@volaharbor.example
      </li>
    </ul>
  </section>

</div>
</body>
</html>
```